Präsentationsvorlagen für psychologische Weiterbildung, Unterstützung und Prävention der psychischen Gesundheit
Zielgruppe
VitaKlar steht für die psychologische Weiterbildung, Unterstützung und Prävention der psychischen Gesundheit.
Für das Erstellen einer geeigneten Präsentation unserer Dienstleistung sind wir auf der Suche nach einer modernen Präsentationsvorlage.
Aufgabenstellung
Wenn möglich die Farben des Logos berücksichtigen.
Folgeprojekte sind Geschäftsbriefe und Broschüre.

```html
<!DOCTYPE html>
<html lang="de">
<head>
<meta charset="utf-8">
<title>VitaKlar – Präsentationsvorlage</title>
<link rel="stylesheet" href="https://fonts.googleapis.com/css2?family=Roboto:wght@400;500;700&display=swap">
<style>
:root{
  --navy:#0d4257;
  --navy-deep:#0a3447;
  --orange:#f47b20;
  --grey:#8a8f94;
  --ink:#2c3a44;
  --line:#c9d3d8;
  --row:#ededed;
  --basic:#3d2c8d;
  --pro:#27b24a;
  --pop:#45c4cf;
  --xtreme:#f0566f;
  --ultimate:#f5863f;
  --lilac:#cfcbe9;
}
*{box-sizing:border-box;margin:0;padding:0}
html,body{width:1200px;height:2185px;overflow:hidden;background:#fff}
body{font-family:"Roboto",Arial,sans-serif;color:var(--ink)}
.deck{position:relative;width:1200px;height:2185px;display:grid;grid-template-columns:580px 580px;grid-auto-rows:326px;column-gap:15px;row-gap:24px;padding:56px 12px 0 13px}
.slide{position:relative;overflow:hidden;background:#fff;box-shadow:0 1px 4px rgba(0,0,0,.18)}
.bar{position:absolute;left:0;top:0;width:100%;height:53px;background:var(--navy);display:flex;align-items:center}
.dots{width:28px;height:28px;margin-left:8px;background:radial-gradient(circle,rgba(255,255,255,.7) 1px,transparent 1.3px) 0 0/4.6px 4.6px}
.bar-title{margin-left:11px;color:#fff;font-weight:700;font-size:11px;letter-spacing:.1px}
.brand{position:absolute;right:18px;top:50%;transform:translateY(-50%);color:var(--orange);font-size:20px;font-weight:400}
.photo{position:absolute;top:53px;bottom:0}
.kicker{position:absolute;color:var(--orange);font-weight:700;font-size:7px;letter-spacing:1px}
.headline{position:absolute;color:var(--navy);font-weight:700;font-size:20px}
.body{position:absolute;color:var(--grey);font-size:6.4px;line-height:11px}
.just{text-align:justify}
/* cover */
.cover{background:linear-gradient(135deg,#123f5a 0%,#0e4a66 50%,#0b3349 100%)}
.cover-art{position:absolute;inset:0;background:radial-gradient(circle at 52% 35%,rgba(90,150,190,.35),transparent 45%)}
.cover-brand{position:absolute;left:144px;top:140px;color:#fff;font-size:62px;font-weight:400}
.cover-info{position:absolute;top:286px;left:0;width:100%;color:#fff;font-size:5.5px;font-weight:500}
.cover-info span{position:absolute;display:flex;align-items:center;gap:4px}
/* toc */
.toc{position:absolute;left:18px;right:52px;top:125px}
.toc-row{display:flex;align-items:center;height:20.3px;font-size:8px;color:var(--ink)}
.toc-row i{flex:1;height:1px;background:#8fa5b0;margin:0 12px 0 8px}
.toc-row b{font-weight:400;width:12px;text-align:right}
/* agenda */
.time{position:absolute;top:172px;width:98px;height:68px;background:var(--navy);color:#fff;font-size:26px;font-weight:500;display:flex;align-items:center;justify-content:center}
.time.now{background:var(--orange);top:174px}
.time-note{position:absolute;top:256px;width:118px;font-size:7px;line-height:10px;text-align:center;color:var(--ink)}
/* checklist */
.check{position:absolute;left:35px;display:flex;align-items:center;gap:12px;color:var(--navy);font-weight:700;font-size:7.5px}
.check svg{width:11px;height:11px}
.focus{position:absolute;left:31px;display:flex;align-items:center;gap:8px;color:var(--orange);font-weight:700;font-size:14.5px}
.focus i{width:19px;height:19px;border-radius:50%;background:#fad3d5;display:flex;align-items:center;justify-content:center}
.focus i::after{content:"";width:8px;height:8px;border-radius:50%;background:var(--orange)}
/* stats */
.stat{position:absolute;top:238px;display:flex;gap:6px}
.stat-num{color:var(--orange);font-size:15px;font-weight:500}
.stat-lab{font-size:6.5px;color:var(--grey);margin-top:4px;text-align:center}
/* features */
.feat{position:absolute;display:flex;gap:8px;align-items:flex-start;color:var(--navy);font-size:6.6px;line-height:11px}
.feat svg{width:20px;height:20px;flex:none}
.ticks{position:absolute;left:265px;color:var(--orange);font-size:5.6px;display:flex;align-items:center;gap:7px}
.ticks svg{width:14px;height:14px}
/* pricing */
.price{position:absolute;left:11px;top:86px;width:559px;border-collapse:collapse;table-layout:fixed}
.price th{height:34px;color:#fff;font-weight:400;font-size:12px}
.price td{height:27px;text-align:center;font-size:9px;color:var(--ink);border-bottom:1px solid #e3e3e3;border-right:1px solid #e3e3e3}
.price td:first-child{border-left:1px solid #e3e3e3}
.price tr.cost td{font-weight:500;font-size:10.5px;height:30px}
/* data table */
.data{position:absolute;left:16px;top:74px;width:545px;border-collapse:collapse;table-layout:fixed;border-bottom:1px solid #333}
.data th{height:39px;background:var(--orange);color:#fff;font-size:8px;font-weight:700;border-top:2px solid #d8640f}
.data td{height:39px;font-size:5.8px;padding-left:2px;color:#222}
.data tr:nth-child(odd) td{background:var(--row)}
/* contact */
.map{position:absolute;left:0;top:53px;width:100%;height:142px;background:linear-gradient(160deg,#eef0ec,#e3e8e1 60%,#cfe3ea)}
.card{position:absolute;top:256px;width:132px;height:51px;background:#fff;box-shadow:0 1px 6px rgba(0,0,0,.12);display:flex;align-items:center;gap:8px;padding-left:22px;font-size:6.4px;color:var(--grey);font-weight:500}
.card i{width:25px;height:25px;border-radius:50%;display:flex;align-items:center;justify-content:center}
.card svg{width:13px;height:13px}
</style>
</head>
<body>
<main class="deck">

  <!-- 1 cover -->
  <section class="slide cover">
    <div class="cover-art" role="img" aria-label="Blaues Hintergrundbild mit Gehirn und Lichtpunkten"></div>
    <div class="cover-brand">VitaKlar</div>
    <div class="cover-info">
      <span style="left:76px"><svg width="7" height="7" viewBox="0 0 10 10"><circle cx="5" cy="5" r="4" fill="none" stroke="#fff"/></svg>WWW.VITAKLAR</span>
      <span style="left:176px"><svg width="8" height="6" viewBox="0 0 10 7"><rect width="10" height="7" fill="#fff"/></svg>INFO@VITAKLAR</span>
      <span style="left:267px"><svg width="6" height="8" viewBox="0 0 6 8"><path d="M3 8 0.5 3.5A2.6 2.6 0 1 1 5.5 3.5Z" fill="#fff"/></svg>MY ADDRESS WILL BE HERE 786</span>
      <span style="left:432px"><svg width="7" height="7" viewBox="0 0 10 10"><path d="M2 0 4 3 3 4.5Q5 7 5.5 7L7 6 10 8 8.5 10Q2 9 0 1.5Z" fill="#fff"/></svg>+49 301 234 567</span>
    </div>
  </section>

  <!-- 2 toc -->
  <section class="slide">
    <header class="bar"><div class="dots"></div><h2 class="bar-title">INHALTSVERZEICHNIS</h2><div class="brand">VitaKlar</div></header>
    <div class="toc">
      <div class="toc-row">Einführung<i></i><b>02</b></div>
      <div class="toc-row">Geschichten<i></i><b>04</b></div>
      <div class="toc-row">Infografiken<i></i><b>05</b></div>
      <div class="toc-row">Zusammenfassung<i></i><b>06</b></div>
      <div class="toc-row">Kontakte<i></i><b>07</b></div>
    </div>
  </section>

  <!-- 3 agenda -->
  <section class="slide">
    <header class="bar"><div class="dots"></div><h2 class="bar-title">HEUTE AGENDA</h2><div class="brand">VitaKlar</div></header>
    <p class="body" style="left:37px;top:95px;width:515px;color:var(--ink);font-size:6.5px;line-height:13px">Lorem ipsum dolor sit amet, consectetur adipiscing elit, sed do eiusmod tempor incididunt ut labore et dolore magna aliqua. Ut enim ad minim veniam, quis nostrud exercitation ullamco laboris nisi ut aliquip ex ea commodo consequat. Duis aute irure dolor in reprehenderit in voluptate velit esse cillum dolore eu fugiat nulla pariatur. Excepteur sint occaecat cupidatat non proident, sunt in culpa qui officia deserunt mollit anim id est laborum.</p>
    <div class="time" style="left:43px">9:00</div>
    <div class="time" style="left:182px">10:00</div>
    <div class="time" style="left:314px">12:00</div>
    <div class="time now" style="left:446px">02:00</div>
    <p class="time-note" style="left:33px">Et duo ullum iner nislorem ipsum dolor si</p>
    <p class="time-note" style="left:172px">Et duo ullum iner nislorem ipsum dolor si</p>
    <p class="time-note" style="left:304px">Et duo ullum iner nislorem ipsum dolor si</p>
    <p class="time-note" style="left:436px;top:258px">Et duo ullum iner nislorem ipsum dolor si</p>
  </section>

  <!-- 4 who we are -->
  <section class="slide">
    <header class="bar"><div class="dots"></div><h2 class="bar-title">ÜBERSCHRIFT DER HAUPTFOLIE</h2><div class="brand">VitaKlar</div></header>
    <div class="photo" style="left:0;width:221px;background:linear-gradient(160deg,#e8e6e2,#cfcbc5 60%,#b9b3aa)" role="img" aria-label="Foto: Geschäftsleute beim Händedruck, von oben"></div>
    <div class="kicker" style="left:248px;top:88px">WILLKOMMEN</div>
    <h3 class="headline" style="left:248px;top:98px">WER SIND WIR?</h3>
    <p class="body just" style="left:248px;top:130px;width:301px">Lorem ipsum dolor sit amet, consectetur adipiscing elit, sed do eiusmod tempor incididunt ut labore et dolore magna aliqua. Ut enim ad minim veniam, quis nostrud exercitation ullamco laboris nisi ut aliquip ex ea commodo consequat. Duis aute irure dolor in reprehenderit in voluptate velit esse cillum dolore eu fugiat nulla pariatur. Excepteur sint occaecat cupidatat non proident, sunt in culpa qui officia deserunt mollit anim id est laborum.</p>
    <p class="body just" style="left:248px;top:213px;width:301px">Sed ut perspiciatis unde omnis iste natus error sit voluptatem accusantium doloremque laudantium, totam rem aperiam, eaque ipsa quae ab illo inventore veritatis et quasi architecto beatae vitae dicta sunt explicabo.</p>
  </section>

  <!-- 5 values -->
  <section class="slide">
    <header class="bar"><div class="dots"></div><h2 class="bar-title">ÜBERSCHRIFT DER HAUPTFOLIE</h2><div class="brand">VitaKlar</div></header>
    <div class="kicker" style="left:38px;top:81px">UNSERE</div>
    <h3 class="headline" style="left:35px;top:92px">GRUNDWERTE</h3>
    <p class="body just" style="left:35px;top:126px;width:239px">Fusce vehicula dolor arcu, sit amet blandit dolor mollis nec. Donec viverra eleifend lacus, vitae ullamcorper metus. Sed sollicitudin ipsum quis nunc sollicitudin ultrices. Donec euismod scelerisque ligula. Maecenas eu varius risus, eu aliquet arcu. Curabitur fermentum suscipit est, tincidunt</p>
    <div class="check" style="top:216px"><svg viewBox="0 0 12 12"><circle cx="6" cy="6" r="6" fill="#e6f3ea"/><path d="M3.2 6.2 5.2 8 8.8 4" fill="none" stroke="#1f8a4c" stroke-width="1.5"/></svg>Proin et risus id eros pharetra commodo.</div>
    <div class="check" style="top:244px"><svg viewBox="0 0 12 12"><circle cx="6" cy="6" r="6" fill="#e6f3ea"/><path d="M3.2 6.2 5.2 8 8.8 4" fill="none" stroke="#1f8a4c" stroke-width="1.5"/></svg>Donec auctor metus sit amet velit blandit sollicitudin.</div>
    <div class="check" style="top:272px"><svg viewBox="0 0 12 12"><circle cx="6" cy="6" r="6" fill="#e6f3ea"/><path d="M3.2 6.2 5.2 8 8.8 4" fill="none" stroke="#1f8a4c" stroke-width="1.5"/></svg>Lorem ipsum dolor sit amet, consectetur adipiscing elit.</div>
    <div class="photo" style="left:352px;right:0;background:linear-gradient(150deg,#eeeae4,#c9a36b 55%,#5a4636)" role="img" aria-label="Foto: Holzwürfel mit dem Wort Goals und Lupe"></div>
  </section>

  <!-- 6 services -->
  <section class="slide">
    <header class="bar"><div class="dots"></div><h2 class="bar-title">UNSERE LEISTUNG</h2><div class="brand">VitaKlar</div></header>
    <div class="photo" style="left:0;width:228px;background:linear-gradient(150deg,#9a9a9a,#c8c8c8 50%,#7d7d7d)" role="img" aria-label="Schwarzweißfoto: Beratungsgespräch mit Klemmbrett"></div>
    <div class="kicker" style="left:263px;top:117px">ZWISCHENÜBERSCHRIFT</div>
    <h3 class="headline" style="left:263px;top:128px">HAUPTÜBERSCHRIFT</h3>
    <p class="body" style="left:263px;top:164px;width:245px">Fusce vehicula dolor arcu, sit amet blandit dolor mollis nec. Donec viverra eleifend lacus, vitae ullamcorper metus sed rockue eleifan.</p>
    <div class="stat" style="left:263px">
      <svg width="22" height="18" viewBox="0 0 22 18"><path d="M5 1h12l4 5-10 11L1 6z M1 6h20 M8 1 6 6l5 11 5-11-2-5" fill="none" stroke="#f47b20" stroke-width="1"/></svg>
      <div><div class="stat-num">1550 +</div><div class="stat-lab">Lorem Ipsum</div></div>
    </div>
    <div class="stat" style="left:380px">
      <svg width="22" height="20" viewBox="0 0 22 20"><g fill="none" stroke="#f47b20" stroke-width="1"><circle cx="5" cy="5" r="2.5"/><circle cx="11" cy="4" r="3"/><circle cx="17" cy="5" r="2.5"/><path d="M2 18V10h6v8M8 19V9h6v10M14 18v-8h6v8"/></g></svg>
      <div><div class="stat-num">1024 +</div><div class="stat-lab">Zufriedene Kunden</div></div>
    </div>
  </section>

  <!-- 7 patient care -->
  <section class="slide">
    <header class="bar"><div class="dots"></div><h2 class="bar-title">ÜBERSCHRIFT DER HAUPTFOLIE</h2><div class="brand">VitaKlar</div></header>
    <div class="kicker" style="left:31px;top:77px">WIE ES UNS GEHT</div>
    <h3 class="headline" style="left:31px;top:89px;font-size:14.5px">PATIENTENVERSORGUNG</h3>
    <p class="body just" style="left:31px;top:114px;width:276px">Lorem ipsum dolor sit amet, consectetur adipiscing elit. Morbi et rutrum felis, eget tristique tortor. Maecenas lobortis mattis turpis ut hendrerit. Fusce placerat ipsum at dictum lobortis. Etiam porta nunc sit amet pellentesque feugiat. Nunc gravida sapien eu tempor lacinia.</p>
    <div class="focus" style="top:185px"><i></i>Schätze dich selbst</div>
    <div class="focus" style="top:215px"><i></i>Beruhige deinen Geist</div>
    <div class="focus" style="top:246px"><i></i>Realistische Ziele</div>
    <div class="focus" style="top:277px"><i></i>Lächle oft</div>
    <div class="photo" style="left:337px;right:0;background:linear-gradient(160deg,#dfe4ea,#a7b2a5 45%,#7a5a4c)" role="img" aria-label="Foto: Patientin im Gespräch mit einer Therapeutin"></div>
  </section>

  <!-- 8 features -->
  <section class="slide">
    <header class="bar"><div class="dots"></div><h2 class="bar-title">ÜBERSCHRIFT DER HAUPTFOLIE</h2><div class="brand">VitaKlar</div></header>
    <div style="position:absolute;left:14px;top:70px;width:240px;height:240px;background:linear-gradient(135deg,#0d4257 0%,#0d4257 45%,#cfcbe9 55%,#e8e6f5)" role="img" aria-label="Illustration: fröhliche und traurige Maske mit Pfeilen"></div>
    <div class="kicker" style="left:265px;top:83px">ZWISCHENÜBERSCHRIFT</div>
    <h3 class="headline" style="left:265px;top:94px">HAUPTÜBERSCHRIFT</h3>
    <div class="feat" style="left:268px;top:142px"><svg viewBox="0 0 20 20"><g fill="none" stroke="#0d4257"><circle cx="10" cy="10" r="9"/><path d="M10 5v10M5 10h10"/></g></svg><span>Synth chartreuse XOXO,<br>tacos brooklyn VHS plaid.</span></div>
    <div class="feat" style="left:420px;top:142px"><svg viewBox="0 0 20 20"><path d="M10 17 3 9.5A4 4 0 0 1 10 5a4 4 0 0 1 7 4.5z" fill="none" stroke="#0d4257"/></svg><span>Synth chartreuse XOXO,<br>tacos brooklyn VHS plaid.</span></div>
    <div class="feat" style="left:268px;top:201px"><svg viewBox="0 0 20 20"><g fill="none" stroke="#0d4257"><circle cx="10" cy="6" r="4"/><path d="M2 19c0-5 4-8 8-8s8 3 8 8z"/></g></svg><span>Synth chartreuse XOXO,<br>tacos brooklyn VHS plaid.</span></div>
    <div class="feat" style="left:420px;top:201px"><svg viewBox="0 0 20 20"><path d="M7 2h6M8 2v6L3 17h14L12 8V2" fill="none" stroke="#0d4257"/></svg><span>Synth chartreuse XOXO,<br>tacos brooklyn VHS plaid.</span></div>
    <p class="body" style="left:268px;top:256px;width:265px;color:var(--ink)">Sed ut perspiciatis unde omnis iste natus error sit voluptatem accusantium doloremque laudantium, totam rem aperiam, eaque ipsa quae ab illo inventore veritatis et quasi architecto beatae vitae dicta sunt explicabo.</p>
  </section>

  <!-- 9 care text -->
  <section class="slide">
    <header class="bar"><div class="dots"></div><h2 class="bar-title">ÜBERSCHRIFT DER HAUPTFOLIE</h2><div class="brand">VitaKlar</div></header>
    <div style="position:absolute;left:22px;top:78px;width:220px;height:232px;background:linear-gradient(160deg,#f47b20 0%,#dde2ea 35%,#d4d9e2 70%,#0d4257 100%)" role="img" aria-label="Illustration: Kopfprofil mit Erste-Hilfe-Koffer und Häkchen"></div>
    <div class="kicker" style="left:265px;top:81px">ZWISCHENÜBERSCHRIFT</div>
    <h3 class="headline" style="left:265px;top:92px">HAUPTÜBERSCHRIFT</h3>
    <p class="body" style="left:265px;top:120px;width:300px;color:var(--ink)">Sed ut perspiciatis unde omnis iste natus error sit voluptatem accusantium doloremque laudantium, totam rem aperiam, eaque ipsa quae ab illo inventore veritatis et quasi architecto beatae vitae dicta sunt explicabo.</p>
    <p class="body" style="left:265px;top:163px;width:300px;color:var(--ink);font-weight:700">Hashtag fashion axe fingerstache, everyday carry shoreditch pinterest umami authentic brooklyn YOLO heirloom keytar waistcoat kickstarter. Kitsch authentic offal, narwhal tilde etsy four loko selvage normcore messenger bag put a bird on it heirloom gastropub.</p>
    <div class="ticks" style="top:226px"><svg viewBox="0 0 14 14"><g fill="none" stroke="#f47b20" stroke-width=".8"><circle cx="7" cy="7" r="6.5"/><path d="M4 7.2 6 9l4-4"/></g></svg>Mauris imperdiet orci vitae volutpat condimentum.</div>
    <div class="ticks" style="top:251px"><svg viewBox="0 0 14 14"><g fill="none" stroke="#f47b20" stroke-width=".8"><circle cx="7" cy="7" r="6.5"/><path d="M4 7.2 6 9l4-4"/></g></svg>Proin sed felis sagittis, fringilla nisi a, egestas felis.</div>
    <div class="ticks" style="top:275px"><svg viewBox="0 0 14 14"><g fill="none" stroke="#f47b20" stroke-width=".8"><circle cx="7" cy="7" r="6.5"/><path d="M4 7.2 6 9l4-4"/></g></svg>Duis hendrerit odio sit amet aliquam finibus.</div>
    <div class="ticks" style="top:299px"><svg viewBox="0 0 14 14"><g fill="none" stroke="#f47b20" stroke-width=".8"><circle cx="7" cy="7" r="6.5"/><path d="M4 7.2 6 9l4-4"/></g></svg>Nullam porttitor orci ac tortor pulvinar pellentesque.</div>
  </section>

  <!-- 10 pricing -->
  <section class="slide">
    <header class="bar"><div class="dots"></div><h2 class="bar-title">TABELLENBEISPIELE</h2><div class="brand">VitaKlar</div></header>
    <table class="price">
      <tr><th style="background:var(--basic)">Basic Plan</th><th style="background:var(--pro)">Professional</th><th style="background:var(--pop)">Popular</th><th style="background:var(--xtreme)">Xtreme</th><th style="background:var(--ultimate)">Ultimate</th></tr>
      <tr><td>First Service</td><td>First Service</td><td>First Service</td><td>First Service</td><td>First Service</td></tr>
      <tr><td>-</td><td>Second Service</td><td>Second Service</td><td>Second Service</td><td>Second Service</td></tr>
      <tr><td>-</td><td>-</td><td>Third Service</td><td>Third Service</td><td>Third Service</td></tr>
      <tr><td>-</td><td>-</td><td>-</td><td>Fourth Service</td><td>Fourth Service</td></tr>
      <tr><td>-</td><td>-</td><td>-</td><td>-</td><td>Fifth Service</td></tr>
      <tr class="cost"><td>€9.99</td><td>€19.99</td><td>€49.99</td><td>€79.99</td><td>€99.99</td></tr>
    </table>
  </section>

  <!-- 11 data table -->
  <section class="slide">
    <header class="bar"><div class="dots"></div><h2 class="bar-title">TABELLENBEISPIELE</h2><div class="brand">VitaKlar</div></header>
    <table class="data">
      <thead><tr><th>Table Header</th><th>Table Header</th><th>Table Header</th><th>Table Header</th></tr></thead>
      <tbody>
        <tr><td>Text here</td><td>Text here</td><td>Text here</td><td>Text here</td></tr>
        <tr><td>Text here</td><td>Text here</td><td>Text here</td><td>Text here</td></tr>
        <tr><td>Text here</td><td>Text here</td><td>Text here</td><td>Text here</td></tr>
        <tr><td>Text here</td><td>Text here</td><td>Text here</td><td>Text here</td></tr>
        <tr><td>Text here</td><td>Text here</td><td>Text here</td><td>Text here</td></tr>
      </tbody>
    </table>
  </section>

  <!-- 12 contact -->
  <section class="slide">
    <header class="bar"><div class="dots"></div><h2 class="bar-title">IN KONTAKT KOMMEN!</h2><div class="brand">VitaKlar</div></header>
    <div class="map" role="img" aria-label="Stadtplan mit Standortmarkierungen"></div>
    <p class="body" style="left:140px;top:214px;width:300px;text-align:center;line-height:13px">Fusce vehicula dolor arcu, sit amet blandit dolor mollis nec. Donec viverra eleifend lacus arcu, sit amet blandit dolor mollis nec lacus.</p>
    <div class="card" style="left:45px"><i style="background:var(--navy)"><svg viewBox="0 0 14 14"><rect x="1" y="3" width="12" height="8" fill="#fff"/><path d="M1 3l6 4.5L13 3" fill="none" stroke="#0d4257"/></svg></i>info@vitaklar</div>
    <div class="card" style="left:225px"><i style="background:var(--orange)"><svg viewBox="0 0 14 14"><path d="M3 1 5.5 4.5 4.2 6Q6 9 8 9.8L9.5 8.5 13 11l-1.8 2Q3 12 1 3z" fill="#fff"/></svg></i>+49 301 234 568</div>
    <div class="card" style="left:407px"><i style="background:#1d5f7a"><svg viewBox="0 0 14 14"><g fill="none" stroke="#fff" stroke-width="1.4"><rect x="1.5" y="5" width="6" height="4" rx="2" transform="rotate(-45 4.5 7)"/><rect x="6.5" y="5" width="6" height="4" rx="2" transform="rotate(-45 9.5 7)"/></g></svg></i>www.vitaklar</div>
  </section>

</main>
</body>
</html>
```